Business card for a restaurant/bar

We are looking for a business card design/template for TANKO Riverside that can be a starting point for a corporate identity pack. We are known for live bands on the weekends, sports, burgers, beers and American cuisine. We have a relaxing/friendly environment and our tag line is "No 'tudes. Just sports, great food, great music and great times." We are located down the street from a college campus and we attract a wide variety of customers from college students, business professionals, and those interested in sports and general trivia.
Visit our website: www.tankoriverside-example.com and see the attached files for more info about us.
Please use the current logo.

```html
<!DOCTYPE html>
<html lang="en">
<head>
<meta charset="utf-8">
<title>TANKO Riverside – Business Card</title>
<link rel="stylesheet" href="https://fonts.googleapis.com/css2?family=Alfa+Slab+One&display=swap">
<style>
  :root {
    --card-black: #000000;
    --ink-white: #ffffff;
    --accent-red: #e3101a;
    --art-light: #f4f4f4;
    --art-mid: #9a9a9a;
  }
  html, body {
    margin: 0;
    padding: 0;
    width: 1200px;
    height: 686px;
    overflow: hidden;
    background: var(--card-black);
  }
  .card {
    position: relative;
    width: 1200px;
    height: 686px;
    background: var(--card-black);
    overflow: hidden;
    font-family: "Alfa Slab One", Georgia, serif;
    color: var(--ink-white);
  }
  .card__rules {
    position: absolute;
    inset: 0;
  }
  .card__portrait {
    position: absolute;
    left: 0;
    top: 0;
    width: 478px;
    height: 686px;
    background: linear-gradient(160deg, var(--art-light) 0%, var(--art-light) 45%, var(--art-mid) 100%);
  }
  .card__details {
    position: absolute;
    right: 69px;
    top: 108px;
    text-align: right;
    font-variant: small-caps;
    font-size: 35px;
    line-height: 38px;
  }
  .card__details p { margin: 0; }
  .card__hours { margin-top: 31px !important; }
  .card__web {
    position: absolute;
    right: 69px;
    top: 603px;
    margin: 0;
    color: var(--accent-red);
    font-size: 17px;
    letter-spacing: 0.3px;
    text-transform: uppercase;
  }
</style>
</head>
<body>
  <main class="card">
    <svg class="card__rules" width="1200" height="686" viewBox="0 0 1200 686" aria-hidden="true">
      <rect x="470" y="14" width="730" height="5" fill="var(--accent-red)"/>
      <rect x="470" y="665" width="730" height="5" fill="var(--accent-red)"/>
    </svg>

    <div class="card__portrait" role="img" aria-label="Black and white poster-style illustration of a smiling man in a suit raising a drink"></div>

    <section class="card__details">
      <p>418 North Campus View Blvd.</p>
      <p>Riverside, CA</p>
      <p>951.555.0142</p>
      <p class="card__hours">Mon-Fri: 11am - 2 am</p>
      <p>Sat-Sun: 8am - 2 am</p>
    </section>

    <p class="card__web">www.tankoriverside-example.com</p>
  </main>
</body>
</html>
```